Allies in Wellness Groupworks- Medical Billing and Consultant Firm Business card

We need a logo design for a medical billing and healthcare consulting firm. We help physician medical practices achieve their financial objectives by providing medical billing services and other revenue cycle services. We want a business card design that is eye catching and compliments the color and design my logo. We like variations of blue colors however we are very open to other colors. We would like the services we provide listed on the back of the card.

Target Market(s)

Doctors and medical practices

Industry/Entity Type

Medical

Contact Information for Business Card

Space for logo, name, title, phone #, address, web address

Font styles to use
Serif
Sans Serif

Colors

Designer to choose colors to be used in the design.

Requirements
Must have
• Company Services listed on the back.
Should not have
• We are pretty open to all design ideas

```html
<!DOCTYPE html>
<html lang="en">
<head>
<meta charset="utf-8">
<title>Allies in Wellness Groupworks — Business Card</title>
<link rel="stylesheet" href="https://fonts.googleapis.com/css2?family=Arimo:wght@400;500&family=Cinzel:wght@500&display=swap">
<style>
  :root {
    --canvas: #e9e7e3;
    --brand-blue: #1559b3;
    --brand-blue-deep: #0f4a9c;
    --brand-blue-light: #2f7fd0;
    --accent-sky: #2aa3dc;
    --paper: #fbfbfa;
    --ink: #1d1d1f;
    --white: #ffffff;
  }
  * { box-sizing: border-box; margin: 0; padding: 0; }
  html, body { width: 1200px; height: 901px; overflow: hidden; }
  body {
    background: var(--canvas);
    display: flex;
    align-items: center;
    justify-content: center;
    gap: 44px;
    font-family: "Arimo", Arial, sans-serif;
  }
  .card {
    width: 525px;
    height: 300px;
    border-radius: 3px;
    overflow: hidden;
    box-shadow: 0 6px 18px rgba(0,0,0,.18);
    position: relative;
  }

  /* Front */
  .card-front { background: var(--paper); }
  .front-band {
    height: 112px;
    background: var(--brand-blue);
    display: flex;
    align-items: center;
    padding-left: 34px;
    gap: 14px;
  }
  .brand-dot {
    width: 26px; height: 26px;
    border-radius: 50%;
    background: var(--white);
    flex: none;
  }
  .brand-name {
    font-family: "Cinzel", Georgia, serif;
    font-weight: 500;
    color: var(--white);
    font-size: 19px;
    line-height: 1.12;
    letter-spacing: .5px;
  }
  .front-body { padding: 26px 0 0 150px; }
  .person-name {
    font-size: 28px;
    font-weight: 400;
    color: var(--brand-blue);
    letter-spacing: .3px;
    line-height: 1;
  }
  .person-title {
    font-size: 15px;
    color: var(--accent-sky);
    margin-top: 3px;
  }
  .contact-list {
    list-style: none;
    margin-top: 16px;
    font-size: 11.5px;
    color: var(--ink);
    line-height: 1.55;
  }

  /* Back */
  .card-back {
    background: linear-gradient(160deg, var(--brand-blue-light) 0%, var(--brand-blue) 45%, var(--brand-blue-deep) 100%);
    color: var(--white);
    text-align: center;
  }
  .back-brand {
    display: flex;
    align-items: center;
    justify-content: center;
    gap: 12px;
    margin-top: 26px;
  }
  .back-brand .brand-name { text-align: left; font-size: 17px; }
  .back-brand .brand-dot { width: 22px; height: 22px; }
  .services-heading {
    font-size: 15px;
    font-weight: 500;
    margin-top: 24px;
    letter-spacing: .3px;
  }
  .services-list {
    list-style: none;
    font-size: 13.5px;
    line-height: 1.5;
    margin-top: 4px;
  }
</style>
</head>
<body>
  <section class="card card-front" aria-label="Business card front">
    <header class="front-band">
      <span class="brand-dot"></span>
      <div class="brand-name">Allies in Wellness<br>Groupworks LLC</div>
    </header>
    <div class="front-body">
      <h1 class="person-name">Mara Quinlan</h1>
      <p class="person-title">Sales manager</p>
      <ul class="contact-list">
        <li>(415) 555-0192</li>
        <li>(415) 555-0178</li>
        <li>mara@allieswellness.com</li>
        <li>www.allieswellness.com</li>
        <li>48 Harbor Lane, Westbrook NY 12045</li>
      </ul>
    </div>
  </section>

  <section class="card card-back" aria-label="Business card back">
    <div class="back-brand">
      <span class="brand-dot"></span>
      <div class="brand-name">Allies in Wellness<br>Groupworks LLC</div>
    </div>
    <h2 class="services-heading">Services Include:</h2>
    <ul class="services-list">
      <li>Medical Billing</li>
      <li>A/R management</li>
      <li>Medical coding by Certified Professional Coders</li>
      <li>Coding and documentation audit</li>
      <li>Revenue cycle assessment</li>
      <li>Site survey</li>
      <li>Data Flow Assessment</li>
    </ul>
  </section>
</body>
</html>
```